Packing for Razor Blade VELKORN

Dears: We need a packing design. The product is an Disposable Razor Blade. We are a company in Brazil.

The packing consists in a bag package which the Disposables Razos are placed. 5 units into each bag.

The bag is not 100% printed and should let a space to the customer see the razors inside. Some competitors uses oval circle. I attached competitor package (Dov Harborline)

The background color should be blue, this color tonality should vary its magnitude from dark blue to soft blue. Blue is a good color for personal care products because customer can take the impression of cleanness, especially for razor blade which has the fuction to shave.

You can feel free to add other colors however it can not be much colorfull because it may get trouble to printer company print it. Silver is good.

You can feel free to do details. You can feel free also to place the logo above the package or at bottom of it.

Dimmensions:
Heigh 24cm
Width 10cm

Featuring
- Featuring: Handle with Grip. In Portuguese - (Cabo Aderente)
- Featuring: 2 Razors. In portuguese - (Duas Lâminas)

Reason: I stayed many days with out providing feedbacks. I want to give more time for you .

Target Market(s)

Mans ( for woman we will design other package )

Requirements
Nice to have
• maybe some tears as a wet surface...
pls can feel free

```html
<!DOCTYPE html>
<html lang="pt">
<head>
<meta charset="utf-8">
<title>VELKORN – Embalagem Lâminas Descartáveis</title>
<link rel="stylesheet" href="https://fonts.googleapis.com/css2?family=Archivo+Black&display=swap">
<style>
  :root {
    --page: #ffffff;
    --blue-deep: #0a1a8c;
    --blue-mid: #1b3fd0;
    --blue-soft: #3d86f5;
    --navy-shadow: #0b1466;
    --window: #ffffff;
    --silver: #9a9a9a;
    --silver-light: #d9dce2;
    --ink: #08104a;
    --edge: #e6e6e6;
  }
  html, body {
    margin: 0;
    padding: 0;
    width: 1200px;
    height: 2615px;
    overflow: hidden;
    background: var(--page);
  }
  .canvas {
    position: relative;
    width: 1200px;
    height: 2615px;
    overflow: hidden;
    font-family: "Archivo Black", "Arial Black", sans-serif;
  }
  .package {
    position: absolute;
    left: 71px;
    top: 0;
    width: 1066px;
    height: 2586px;
    background: radial-gradient(ellipse 75% 45% at 45% 40%, var(--blue-soft) 0%, var(--blue-mid) 45%, var(--blue-deep) 100%);
  }
  .package-edge {
    position: absolute;
    left: 71px;
    top: 0;
    width: 18px;
    height: 2586px;
    background: var(--edge);
  }
  .artwork {
    position: absolute;
    left: 0;
    top: 0;
    width: 1200px;
    height: 2615px;
  }
  .count-badge {
    position: absolute;
    left: 286px;
    top: 206px;
    width: 176px;
    height: 160px;
    border-radius: 26px;
    background: var(--window);
    border: 8px solid var(--ink);
    box-sizing: border-box;
    transform: rotate(-6deg);
    display: flex;
    align-items: center;
    justify-content: center;
    font-size: 150px;
    line-height: 1;
    color: var(--blue-deep);
  }
  .badge-label {
    position: absolute;
    left: 190px;
    width: 520px;
    text-align: center;
    font-style: italic;
    color: var(--ink);
    font-size: 44px;
    line-height: 1;
    transform: rotate(-6deg);
  }
  .badge-label.line-1 { top: 408px; }
  .badge-label.line-2 { top: 462px; left: 210px; }
  .features {
    position: absolute;
    left: 71px;
    width: 1066px;
    top: 2016px;
    text-align: center;
    font-style: italic;
    font-size: 52px;
    line-height: 62px;
    color: var(--silver-light);
    -webkit-text-stroke: 3px var(--ink);
    text-shadow: 4px 4px 0 var(--ink);
    letter-spacing: 1px;
  }
  .features p { margin: 0; }
  .brand {
    position: absolute;
    left: 71px;
    width: 1066px;
    top: 2305px;
    text-align: center;
    font-size: 86px;
    line-height: 1;
    color: #ffffff;
    letter-spacing: 2px;
  }
</style>
</head>
<body>
<div class="canvas">
  <div class="package"></div>
  <div class="package-edge"></div>

  <svg class="artwork" viewBox="0 0 420 915.25" preserveAspectRatio="none" aria-hidden="true">
    <!-- hanger slot -->
    <path class="hanger-slot" d="M172 48 V30 Q172 25 177 25 H200 Q204 25 206 29 Q210 33 214 29 Q216 25 220 25 H243 Q248 25 248 30 V48 Z" fill="var(--window)"/>

    <!-- silver badge backdrop -->
    <polygon class="badge-shape" fill="var(--silver)" stroke="var(--window)" stroke-width="3"
      points="120,62 150,72 180,75 205,90 232,118 238,140 230,158 215,172 200,176 180,180 150,185 118,192 98,205 82,222 66,244 70,215 86,190 104,168 90,150 78,130 70,108 88,95 108,78"/>

    <!-- product window shadow -->
    <polygon class="window-shadow" fill="var(--navy-shadow)" transform="translate(8 10)"
      points="240,215 300,180 330,140 360,110 385,80 398,65 398,105 375,130 350,160 325,205 310,240 300,300 340,340 345,360 300,410 325,500 300,560 260,620 210,660 175,680 140,700 100,715 60,730 25,745 25,700 60,690 95,670 130,640 150,600 140,560 100,480 90,430 110,380 105,345 150,340 200,270"/>
    <!-- product window -->
    <polygon class="product-window" fill="var(--window)"
      points="240,215 300,180 330,140 360,110 385,80 398,65 398,105 375,130 350,160 325,205 310,240 300,300 340,340 345,360 300,410 325,500 300,560 260,620 210,660 175,680 140,700 100,715 60,730 25,745 25,700 60,690 95,670 130,640 150,600 140,560 100,480 90,430 110,380 105,345 150,340 200,270"/>
  </svg>

  <div class="count-badge">5</div>
  <div class="badge-label line-1">Descartáveis</div>
  <div class="badge-label line-2">Razors</div>

  <div class="features">
    <p>Cabo Aderente</p>
    <p>3 Lâminas Razors</p>
    <p>Lazer Sharp</p>
  </div>

  <div class="brand">VELKORN</div>
</div>
</body>
</html>
```